The Quick Guard Privacy Handbook

A book cover. The book will be marketed as a promotional item for financial advisors, financial planners, independent insurance agents, bankers, and any professional who views their role as guardian of their clients assets and helping them manage risk.

```html
<!DOCTYPE html>
<html lang="en">
<head>
<meta charset="utf-8">
<title>The Quick Guard Privacy Handbook – Cover</title>
<link href="https://fonts.googleapis.com/css2?family=Montserrat:ital,wght@0,700;0,800;1,700&display=swap" rel="stylesheet">
<style>
  :root {
    --page-bg: #ffffff;
    --cover-blue: #0a72bb;
    --cover-blue-deep: #0a5f9e;
    --accent-yellow: #f2c318;
    --text-white: #ffffff;
    --silhouette: #0b1f3a;
  }
  * { margin: 0; padding: 0; box-sizing: border-box; }
  html, body {
    width: 1200px;
    height: 821px;
    overflow: hidden;
    background: var(--page-bg);
  }
  body {
    display: flex;
    align-items: center;
    justify-content: center;
    font-family: "Montserrat", sans-serif;
  }
  .book-cover {
    position: relative;
    width: 547px;
    height: 821px;
    background: var(--cover-blue);
    color: var(--text-white);
    text-align: center;
  }
  .title {
    position: absolute;
    top: 56px;
    left: 0;
    right: 0;
    font-weight: 800;
    font-size: 50px;
    line-height: 53px;
    letter-spacing: 0.5px;
    text-transform: uppercase;
  }
  .title-line { display: block; }
  .title-line--accent { color: var(--accent-yellow); }
  .title-line--ruled {
    display: flex;
    align-items: center;
    justify-content: center;
    gap: 16px;
  }
  .title-rule {
    width: 70px;
    height: 3px;
    background: var(--accent-yellow);
  }
  .subtitle {
    position: absolute;
    top: 338px;
    left: 0;
    right: 0;
    color: var(--accent-yellow);
    font-style: italic;
    font-weight: 700;
    font-size: 22px;
    line-height: 27px;
  }
  .boardroom-photo {
    position: absolute;
    top: 420px;
    left: 40px;
    right: 40px;
    height: 210px;
    background:
      linear-gradient(180deg, rgba(10,114,187,0) 0%, rgba(11,31,58,0.85) 35%, var(--silhouette) 55%, rgba(11,31,58,0.5) 75%, rgba(10,114,187,0) 100%);
  }
  .tagline {
    position: absolute;
    top: 636px;
    left: 0;
    right: 0;
    font-weight: 700;
    font-size: 17.5px;
    line-height: 23px;
    text-transform: uppercase;
  }
  .author {
    position: absolute;
    top: 733px;
    left: 0;
    right: 0;
    font-weight: 800;
    font-size: 38px;
    line-height: 46px;
  }
</style>
</head>
<body>
  <main class="book-cover">
    <h1 class="title">
      <span class="title-line">The</span>
      <span class="title-line title-line--accent">Quick Guard</span>
      <span class="title-line">Privacy</span>
      <span class="title-line title-line--ruled">
        <span class="title-rule"></span>Handbook<span class="title-rule"></span>
      </span>
    </h1>
    <p class="subtitle">Protect yourself<br>and family in the AI age</p>
    <div class="boardroom-photo" role="img" aria-label="Silhouettes of a business team seated around a boardroom table with reflections on the floor"></div>
    <p class="tagline">It’s better to have it and not need it<br>than need it and not have it.</p>
    <p class="author">Daniel Whitford</p>
  </main>
</body>
</html>
```